Financial PR company Homepage and Inner Page design

Please design a web homepage and innerpage for LORVIA Public Relations.
LORVIA Public Relations is a Financial PR company targeting Shenzhen Qian Special Economical Zone.
Note:
1. Menu includes ( Please specialize in Chinese and we want to see the Chinese fonts)
关于我们/服务板块/专业优势/合作伙伴/前海商圈/公司新闻/加盟我们/联系我们

2. Please refer to world class PR Business company and contribute your idea on website design and color themes.

3. We have attached the Logo for reference.

4. Anytime use picture for reference, please select asian business people pictures.

Cheers,

HI Designers, Thanks for the design submission. Here is our client feedback: 1. Adopt one screen design. 2. Use amiable Asia Business woman pictures. 3. Use contrastive color theme for the design. Cheers, Kit From PW

```html
<!DOCTYPE html>
<html lang="zh-CN">
<head>
<meta charset="utf-8">
<title>LORVIA Public Relations</title>
<link rel="stylesheet" href="https://fonts.googleapis.com/css2?family=Arimo:wght@400;700&family=Noto+Sans+SC:wght@400;500&display=swap">
<style>
:root{
  --navy:#0e1a2b;
  --navy-soft:#1c2e45;
  --sky:#5bc8f0;
  --sky-line:#48b4dc;
  --accent:#3a9bd5;
  --ink:#2b2b2b;
  --muted:#777;
  --panel:#eeeeee;
  --white:#fff;
}
*{margin:0;padding:0;box-sizing:border-box}
html,body{width:713px;height:1200px;overflow:hidden}
body{position:relative;font-family:"Arimo","Noto Sans SC",sans-serif;color:var(--ink);background:var(--white)}
.abs{position:absolute}
.zh{font-family:"Noto Sans SC","Arimo",sans-serif}

.site-header{left:0;top:0;width:713px;height:58px;background:var(--navy)}
.brand{left:84px;top:13px;display:flex;align-items:center;gap:8px;color:var(--white)}
.brand-mark{width:26px;height:26px;border-radius:50%;background:var(--sky)}
.brand-name{font-size:16px;line-height:16px;font-weight:400}
.brand-sub{font-size:7px;line-height:8px;color:#b9d7e8}
.search{left:510px;top:18px;width:125px;height:23px;background:var(--navy-soft);border-radius:2px}
.search svg{position:absolute;right:8px;top:6px}

.main-nav{left:0;top:58px;width:713px;height:31px;background:var(--sky);border-bottom:1px solid var(--sky-line)}
.main-nav a{position:absolute;top:0;height:31px;line-height:31px;font-size:8px;color:var(--navy);text-decoration:none}
.nav-divider{position:absolute;top:0;width:1px;height:31px;background:var(--sky-line)}

.hero{left:0;top:89px;width:713px;height:293px;background:linear-gradient(90deg,#b9d9e6 0%,#e3eff4 35%,#d3e6ee 60%,#a9cddc 100%)}
.hero-photo{left:438px;top:17px;width:168px;height:276px;background:linear-gradient(180deg,#9fb8cf 0%,#5f7ea6 45%,#3c5586 100%)}
.hero-kicker{left:84px;top:74px;font-size:26px;font-weight:700;color:var(--accent);letter-spacing:.5px}
.hero-title{left:84px;top:106px;font-size:15px;line-height:21px;font-weight:400;color:var(--ink);letter-spacing:.3px}
.hero-text{left:83px;top:163px;width:258px;font-size:8.6px;line-height:14.5px;color:#555}
.dots{left:82px;top:225px;display:flex;gap:4px}
.dots i{width:8px;height:8px;border-radius:50%;background:var(--white)}
.dots i:first-child{background:var(--navy)}

.welcome{left:0;top:382px;width:713px;height:194px;background:var(--panel);text-align:center}
.section-title{font-size:19px;font-weight:400;color:var(--ink);letter-spacing:.3px}
.section-title span{color:var(--accent)}
.welcome .section-title{position:absolute;left:0;width:713px;top:52px}
.welcome-text{left:82px;top:88px;width:549px;font-size:8.2px;line-height:14.5px;color:var(--muted)}
.btn{left:321px;top:143px;width:69px;height:24px;line-height:24px;background:#ddd;font-size:8.5px;color:#444;border-radius:2px}

.services{left:0;top:576px;width:713px;height:314px;background:var(--sky)}
.services .section-title{position:absolute;left:0;width:713px;top:33px;text-align:center;font-size:18px}
.card{width:273px;height:97px;background:var(--white)}
.card-icon{position:absolute;left:13px;top:16px;width:30px;height:34px;border-radius:50%}
.card h3{position:absolute;left:57px;top:22px;font-size:10px;font-weight:400;letter-spacing:.3px;color:var(--ink)}
.card p{position:absolute;left:57px;top:41px;width:202px;font-size:7.5px;line-height:14.4px;color:var(--muted)}
.more{color:var(--accent)}

.news .section-title{position:absolute;left:0;width:713px;top:923px;text-align:center;font-size:18px}
.news-photo{width:83px;height:59px}
.news-item h4{position:absolute;font-size:7.5px;font-weight:700;letter-spacing:.2px}
.news-item p{position:absolute;width:160px;font-size:7px;line-height:14px;color:var(--muted)}

.partners{left:0;top:1058px;width:713px;height:62px;background:var(--panel)}
.partner-badge{position:absolute;top:24px;height:14px;background:#8a8a8a;border-radius:2px}

.site-footer{left:0;top:1120px;width:713px;height:80px;background:var(--navy);color:#e5eef4}
.footer-links{left:79px;top:30px;font-size:7px;word-spacing:2px}
.copyright{left:79px;top:52px;font-size:7.5px}
.follow{left:534px;top:26px;font-size:7.5px}
.social{left:532px;top:44px;display:flex;gap:4px}
.social i{width:18px;height:18px;border-radius:50%;background:var(--white)}
</style>
</head>
<body>

<header class="site-header abs">
  <div class="brand abs">
    <span class="brand-mark"></span>
    <div>
      <div class="brand-name">LORVIA PR</div>
      <div class="brand-sub">qianhai pr partners</div>
      <div class="brand-sub zh" style="text-align:right">前海罗维公关</div>
    </div>
  </div>
  <div class="search abs">
    <svg width="10" height="10" viewBox="0 0 10 10"><circle cx="4" cy="4" r="3" fill="none" stroke="#fff" stroke-width="1.5"/><line x1="6.2" y1="6.2" x2="9" y2="9" stroke="#fff" stroke-width="1.6"/></svg>
  </div>
</header>

<nav class="main-nav abs zh">
  <a style="left:87px">关于我们</a><span class="nav-divider" style="left:138px"></span>
  <a style="left:152px">服务板块</a><span class="nav-divider" style="left:203px"></span>
  <a style="left:216px">专业优势</a><span class="nav-divider" style="left:268px"></span>
  <a style="left:286px">合作伙伴</a><span class="nav-divider" style="left:335px"></span>
  <a style="left:352px">前海商圈</a><span class="nav-divider" style="left:402px"></span>
  <a style="left:418px">公司新闻</a><span class="nav-divider" style="left:472px"></span>
  <a style="left:488px">加盟我们</a><span class="nav-divider" style="left:540px"></span>
  <a style="left:555px">联系我们</a>
</nav>

<section class="hero abs">
  <div class="hero-photo abs" role="img" aria-label="Photo of a smiling Asian business professional in a suit"></div>
  <div class="hero-kicker abs">POWERFUL</div>
  <h1 class="hero-title abs">AND EFFECTIVE COOPERATION<br>LASTING FOR YEARS</h1>
  <p class="hero-text abs">Sed ut perspiciatis unde omnis iste natus error sit voluptatem accusantium dolorelaudantium, totam rem aperiam, eaque ipsa quae ab illo inore</p>
  <div class="dots abs"><i></i><i></i><i></i><i></i></div>
</section>

<section class="welcome abs">
  <h2 class="section-title">Welcome to our <span>Site!</span></h2>
  <p class="welcome-text abs">Fusce suscipit varius mi. Cum sociis natoque penatibus et magnis dis parturient montes, nascetur ridiculus mus. Fusce suscipit varius mi. Cum sociis natoque penatibus et magnis dis parturient montes, nascetur ridiculus mus. Fusce suscipit varius mi. Cum sociis natoque penatibus et magnis dis parturient montes, nascetur ridiculus mus.</p>
  <div class="btn abs">Read More</div>
</section>

<section class="services abs">
  <h2 class="section-title">Service Sector</h2>
  <article class="card abs" style="left:77px;top:77px">
    <div class="card-icon" role="img" aria-label="Rising bar chart icon" style="background:linear-gradient(135deg,#e94b3c,#f2b134,#6bbf4e)"></div>
    <h3>DOLOREM IPSUM</h3>
    <p>Fusce suscipit varius mi. Cum sociis natoque penatibus et magnis dis parturient montes, nascetur ridiculus mus. <span class="more">[ Read More ]</span></p>
  </article>
  <article class="card abs" style="left:363px;top:77px">
    <div class="card-icon" role="img" aria-label="Tree with magnifying glass icon" style="background:linear-gradient(135deg,#a6cf4a,#6b8f2a)"></div>
    <h3 style="left:67px">ADIPISICING ELIT</h3>
    <p style="left:67px;width:196px">Fusce suscipit varius mi. Cum sociis natoque penatibus et magnis dis parturient montes, nascetur ridiculus mus. <span class="more">[ Read More ]</span></p>
  </article>
  <article class="card abs" style="left:77px;top:186px">
    <div class="card-icon" role="img" aria-label="Money bag icon" style="background:linear-gradient(135deg,#d9c29a,#9b7f52)"></div>
    <h3>VULPUTATE LACUS</h3>
    <p>Fusce suscipit varius mi. Cum sociis natoque penatibus et magnis dis parturient montes, nascetur ridiculus mus. <span class="more">[ Read More ]</span></p>
  </article>
  <article class="card abs" style="left:363px;top:186px">
    <div class="card-icon" role="img" aria-label="Orange clock icon" style="background:linear-gradient(135deg,#f39c3d,#d25a1c)"></div>
    <h3 style="left:58px">DOLORE MAGNA ALIQU</h3>
    <p style="left:58px;width:202px">Fusce suscipit varius mi. Cum sociis natoque penatibus et magnis dis parturient montes, nascetur ridiculus mus. <span class="more">[ Read More ]</span></p>
  </article>
</section>

<section class="news">
  <h2 class="section-title">Latest <span>News</span></h2>
  <div class="news-item">
    <div class="news-photo abs" role="img" aria-label="Photo of business colleagues talking in an office" style="left:77px;top:963px;background:linear-gradient(90deg,#b9aaa0,#7d8590,#e2e6ea)"></div>
    <h4 style="left:176px;top:967px">DONEC ET ERAT A SEM</h4>
    <p style="left:176px;top:982px">Fusce suscipit varius mi. Cum sociis natoe penatibus et magnis dis parturient montes, nascetur ridiculus mus. <span class="more">[ Read More ]</span></p>
  </div>
  <div class="news-item">
    <div class="news-photo abs" role="img" aria-label="Photo of a business team in an office" style="left:374px;top:963px;background:linear-gradient(90deg,#d8dde0,#9a8676,#cfd6da)"></div>
    <h4 style="left:474px;top:966px">PROIN LOREM SAPIEN</h4>
    <p style="left:474px;top:982px">Fusce suscipit varius mi. Cum sociis natoe penatibus et magnis dis parturient montes, nascetur ridiculus mus. <span class="more">[ Read More ]</span></p>
  </div>
</section>

<section class="partners abs" aria-label="Partners">
  <span class="partner-badge" style="left:84px;width:90px"></span>
  <span class="partner-badge" style="left:205px;width:134px"></span>
  <span class="partner-badge" style="left:374px;width:113px"></span>
  <span class="partner-badge" style="left:527px;width:107px"></span>
</section>

<footer class="site-footer abs">
  <div class="footer-links abs zh">关于我们 / 服务板块 / 专业优势 / 合作伙伴 / 前海商圈 / 公司新闻 / 加盟我们 / 联系我们</div>
  <div class="copyright abs">© 2014. Yoursite. All Right Reserved.</div>
  <div class="follow abs">Follow us</div>
  <div class="social abs"><i></i><i></i><i></i><i></i><i></i></div>
</footer>

</body>
</html>
```